IT consulting company looking for a modern business design for a website and a new logo

We are the IT-consulting company VelTarix from Germany and need a new and modern business website and a new logo. We are specialized in output management. Our services include business analysis, outsourcing, development, training and project leading. We wish for a design with nature pictures (mountains, lakes, rivers, forests, etc.) for our company with the colors green and blue. If it is possible, a slow-mo video of a nature scene. The design should be responsive and the menu should change to a hamburger menu. The following are: • Services / Solutions 1. Output Management 2. Outsourcing 3. Development 4. Business Analyst 5. Training • Partners • Careers • About Us 1. Project A 2. Project B 3. Project C • Contact Notes for the following categories: For "Services / Solutions" we want to conclude some contents from all the sub-points and sub-points below. Additionally, we would like to see some sub-point under "Services / Solutions". For Output Management: "5 Benefits of Output Management Systems (OMS) - OMS Simplifies and Accelerates External Communication - Helps Reduce Communication Mistakes - Provides Customers With Fast and Secure Responses to your questions - Employees can focus on the essential as they can access prepared templates - Companies get complete transparency about their communication "The point" partner does not have sub-points. The content here is a quote and the logo from the company Brin. For now, just placeholders on this site. The next point wants to be "career" without sub-point and wants to contain some text. Carrer options wants to be listed here. Next point wants to be "About us", where we need sub-points which we do not know exactly at this moment, but they will contain text. By clicking directly on "About us" we want to include pictures and texts about 6 employees for which we only need placeholders at the moment. The last point wants to be "contact", where customers can send us messages. The main page should include a story about our company, which can be a placeholder for now. For reference, designs have a look at: https://lumoravex.de/ https://www.trobelink.com/ https://www.pemdarix.de/ We prefer WordPress designs, created with the plugin ELEMENTOR, so that we can easily edit the content by ourselves. The final design should look professional, competent and modern.

Target Market(s)

With our website, we want to reach the following target groups. <br> <br> <br> <br> <br> <br> <br> <br> <br> <br> <br> <br> <br> <br> <br> <br> <br> <br> <br> <br> <br> <br> <br> <br> <br> <br> <br> <br> <br> <br> <br> <br> <br> <br> <br> <br> <br> <br> <br> <br> <br> <br> <br> <br> <br> <br> <br> <br> <br>

Industry/Entity Type

Consulting

Logo Text

(optionally) VelTarix

Font styles to use
Sans Serif

Colors

Designer to choose colors to be used in the design.

Requirements
Must have
• 1. Outsourcing 3. Development 4. Business Analyst 5. Training • Partners • Careers • About Us 1. Project A 2. Project B 3. Project C • Contact The above-mentioned background picture with nature motifs (mountains, lakes, rivers, forests, etc.). WordPress design in primary colors blue and green.
Nice to have
• ELEMENTOR template. Effects for the background pictures. Counter of all successful projects for Output Management, Business Analyst and Training

```html
<!DOCTYPE html>
<html lang="en">
<head>
<meta charset="utf-8">
<title>VelTarix – Output Management</title>
<link href="https://fonts.googleapis.com/css2?family=Poppins:wght@400;500;600;700&family=Open+Sans:wght@400;600&display=swap" rel="stylesheet">
<style>
:root{
  --blue:#1b5ea6;
  --navy:#1d3a5f;
  --green:#8cc63f;
  --green-dark:#6fae2a;
  --ink:#2b2b2b;
  --text:#444;
  --muted:#666;
  --line:#d8dde4;
  --mist:#eef2f8;
  --white:#fff;
}
*{margin:0;padding:0;box-sizing:border-box}
html,body{width:1200px;height:4240px;overflow:hidden;background:var(--white)}
body{font-family:"Poppins",sans-serif;color:var(--text)}
.page{position:relative;width:1200px;height:4240px;overflow:hidden}
.abs{position:absolute}
.brand{display:flex;align-items:center;gap:10px;font-family:"Poppins",sans-serif;font-weight:600;color:var(--blue)}
.brand-dot{border-radius:50%;background:var(--green)}
.btn{position:absolute;display:flex;align-items:center;justify-content:center;background:var(--green);color:var(--white);font-weight:500;font-size:17px}
.section-title{position:absolute;left:0;width:1200px;text-align:center;font-weight:500;color:var(--blue);font-size:37px}
.section-title .accent{color:var(--green)}
.title-mark{position:absolute;left:588px;width:24px;height:24px;border-radius:50%;border:2px solid var(--blue)}
.body-copy{font-family:"Open Sans",sans-serif;font-size:13px;line-height:24px;color:var(--text);text-align:center}

/* hero */
.hero-phone{left:870px;top:26px;color:var(--white);font-size:16px;display:flex;align-items:center;gap:8px}
.hero-menu{left:1026px;top:22px;width:32px;height:32px;border:2px solid var(--white);border-radius:50%}
.hero-menu span{position:absolute;left:8px;width:12px;height:2px;background:var(--white)}
.hero-title{left:141px;top:172px;font-size:48px;line-height:60px;font-weight:500;color:var(--ink)}

/* services */
.card{position:absolute;width:266px;height:198px;background:var(--white);border-radius:10px;box-shadow:0 4px 18px rgba(30,60,100,.12);text-align:center}
.card.active{border:2px solid var(--green)}
.card-icon{position:absolute;left:103px;top:12px;width:60px;height:60px}
.card h3{position:absolute;left:0;width:100%;top:80px;font-size:16px;font-weight:600;color:var(--ink)}
.card p{position:absolute;left:18px;right:18px;top:118px;font-family:"Open Sans",sans-serif;font-size:12.5px;line-height:21px;color:var(--text)}

/* benefits */
.benefit-title{left:141px;top:1836px;font-size:29px;line-height:38px;font-weight:400;color:var(--blue)}
.benefit-title .accent{color:var(--green)}
.benefit-list{left:141px;top:1928px;width:520px;list-style:none;font-family:"Open Sans",sans-serif;font-size:12.5px;line-height:19px;color:var(--text)}
.benefit-list li{position:relative;padding-left:32px}
.benefit-list svg{position:absolute;left:2px;top:2px}

/* team */
.member{position:absolute;width:220px;text-align:center}
.member-photo{margin:0 auto;width:128px;height:128px;border-radius:50%;border:2px solid var(--blue);padding:5px;background:var(--white)}
.member-photo div{width:100%;height:100%;border-radius:50%}
.member h4{margin-top:16px;font-size:16px;font-weight:500;color:var(--blue)}
.member .role{font-size:12.5px;color:var(--muted);margin-top:4px}
.member p{margin-top:12px;font-size:12.5px;line-height:20px;color:var(--muted)}

/* partners */
.partner{position:absolute;top:3104px;width:123px;height:73px;border:1px solid var(--line);border-radius:4px;background:var(--white);display:flex;align-items:center;justify-content:center}
.partner-badge{width:60px;height:26px;border-radius:13px;background:#c9d3de}
.slider-dot{position:absolute;top:3208px;width:24px;height:24px;border:1px solid var(--line);border-radius:50%}

/* contact */
.contact-title{left:571px;top:3420px;font-size:35px;font-weight:600;color:var(--blue)}
.contact-title .accent{color:var(--green)}
.field{position:absolute;border-bottom:1px solid var(--line);height:34px;font-size:11.5px;color:var(--muted);display:flex;align-items:center;gap:12px}
.field .ico{width:14px;height:14px;color:var(--blue)}

/* footer */
.foot-col{position:absolute;top:3992px}
.foot-col h5{font-size:14px;font-weight:500;color:var(--blue)}
.foot-col h5::after{content:"";display:block;width:36px;height:2px;background:var(--blue);margin-top:8px}
.foot-col ul{list-style:none;margin-top:14px;font-size:12.5px;line-height:25.5px;color:var(--text)}
.foot-row{display:flex;gap:12px;font-size:12.5px;line-height:20px;color:var(--text);margin-top:14px}
.copyright{left:0;top:4202px;width:1200px;height:38px;background:var(--blue);color:var(--white);font-size:12.5px;display:flex;align-items:center;justify-content:center}
</style>
</head>
<body>
<div class="page">

  <!-- HERO -->
  <svg class="abs" style="left:0;top:0" width="1200" height="540" aria-hidden="true">
    <path d="M730 0 H1200 V518 C1120 520 1040 505 980 470 C900 430 820 470 770 420 C720 360 760 300 730 240 C700 170 740 90 700 40 Z" fill="var(--navy)"/>
    <path d="M1200 400 C1150 400 1115 440 1120 480 C1125 510 1170 520 1200 518 Z" fill="var(--green)"/>
    <circle cx="1055" cy="490" r="26" fill="var(--green)"/>
  </svg>
  <div class="abs brand" style="left:140px;top:22px;font-size:38px"><span class="brand-dot" style="width:48px;height:48px"></span>VelTarix</div>
  <div class="abs hero-phone">
    <svg width="18" height="18" viewBox="0 0 24 24"><path d="M6.6 10.8a15 15 0 0 0 6.6 6.6l2.2-2.2c.3-.3.7-.4 1-.2 1.1.4 2.3.6 3.6.6.6 0 1 .4 1 1V20c0 .6-.4 1-1 1A17 17 0 0 1 3 4c0-.6.4-1 1-1h3.5c.6 0 1 .4 1 1 0 1.3.2 2.5.6 3.6.1.3 0 .7-.2 1z" fill="none" stroke="#fff" stroke-width="1.8"/></svg>
    123.456.7890
  </div>
  <div class="abs" style="left:1015px;top:22px;width:1px;height:32px;background:rgba(255,255,255,.6)"></div>
  <div class="abs hero-menu"><span style="top:9px"></span><span style="top:14px"></span><span style="top:19px"></span></div>
  <h1 class="abs hero-title">We Are Specialized<br>In Output<br>Management</h1>
  <div class="btn" style="left:143px;top:369px;width:145px;height:49px">View Demo</div>

  <div class="abs" style="left:606px;top:107px;width:410px;height:288px;border-radius:14px;background:#1a1a1a;box-shadow:0 14px 26px rgba(0,0,0,.35)"></div>
  <div class="abs" role="img" aria-label="Video still of a team meeting in a bright office" style="left:640px;top:123px;width:350px;height:256px;background:linear-gradient(160deg,#7e95ad,#3e5a78 60%,#2a4160)"></div>
  <svg class="abs" style="left:777px;top:225px" width="50" height="50" aria-label="Play video" role="img"><circle cx="25" cy="25" r="24" fill="none" stroke="#fff" stroke-width="2.5"/><path d="M20 15 L35 25 L20 35 Z" fill="var(--green)"/></svg>

  <!-- ABOUT -->
  <svg class="abs" style="left:0;top:690px" width="1200" height="290" aria-hidden="true">
    <defs><linearGradient id="mist" x1="0" y1="0" x2="0" y2="1"><stop offset="0" stop-color="#fff"/><stop offset="1" stop-color="#e3e9f3"/></linearGradient></defs>
    <path d="M0 0 H1200 V170 C1100 140 1000 150 880 175 C720 210 620 280 440 270 C260 260 160 200 0 230 Z" fill="url(#mist)"/>
  </svg>
  <h2 class="section-title" style="top:616px;font-weight:600">About <span class="accent">VelTarix</span></h2>
  <div class="title-mark" style="top:671px"></div>
  <p class="abs body-copy" style="left:150px;top:712px;width:900px">Lorem ipsum dolor sit amet, consectetuer adipiscing elit, sed diam nonummy nibh euismod tincidunt ut laoreet dolore magna aliquam erat volutpat. Ut wisi enim ad minim veniam, quis nostrud exerci tation ullamcorper suscipit lobortis nisl ut aliquip ex ea commodo consequat. Duis autem vel eum iriure dolor in hendrerit in vulputate velit esse molestie consequat, vel illum dolore eu feugiat nulla facilisis at vero eros et accumsan et iusto odio dignissim qui blandit praesent luptatum zzril delenit augue duis dolore te feugait nulla facilisi.</p>
  <div class="btn" style="left:525px;top:823px;width:140px;height:39px">Read More</div>

  <!-- SERVICES -->
  <h2 class="section-title" style="top:1030px">Our <span class="accent">Services</span></h2>
  <p class="abs body-copy" style="left:190px;top:1099px;width:820px">Lorem ipsum dolor sit amet, consectetuer adipiscing elit, sed diam nonummy nibh euismod tincidunt ut laoreet dolore magna aliquam erat volutpat. Ut wisi enim ad minim veniam, quis nostrud exerci tation ullamcorper suscipit lobortis nisl</p>

  <div class="card" style="left:141px;top:1185px">
    <svg class="card-icon" viewBox="0 0 60 60" fill="none" stroke="var(--blue)" stroke-width="2.5"><rect x="6" y="8" width="38" height="26" rx="2"/><path d="M18 42h14M25 34v8"/><rect x="38" y="24" width="16" height="26" rx="2" fill="#fff"/><path d="M12 16h26M12 22h18"/></svg>
    <h3>Output Management</h3>
    <p>Lorem ipsum dolor sit amet, consectetuer adipiscing elit, sed diam nonummy nibh euismod tincidunt</p>
  </div>
  <div class="card active" style="left:469px;top:1185px">
    <svg class="card-icon" viewBox="0 0 60 60" fill="none" stroke="var(--blue)" stroke-width="2.5"><circle cx="30" cy="30" r="14"/><circle cx="30" cy="30" r="5"/><path d="M30 6v10M30 44v10M6 30h10M44 30h10M13 13l7 7M40 40l7 7M13 47l7-7M40 20l7-7"/></svg>
    <h3>Outsourcing</h3>
    <p>Lorem ipsum dolor sit amet, consectetuer adipiscing elit, sed diam nonummy nibh euismod tincidunt</p>
  </div>
  <div class="card" style="left:795px;top:1185px">
    <svg class="card-icon" viewBox="0 0 60 60" fill="none" stroke="var(--blue)" stroke-width="2.5"><path d="M20 40 C20 22 34 10 50 8 C48 24 36 38 20 40Z"/><circle cx="37" cy="22" r="4"/><path d="M20 40l-8 8M14 32l-6 2M28 46l-2 6"/><circle cx="44" cy="44" r="7"/></svg>
    <h3 style="top:86px">Entwicklung</h3>
    <p>Lorem ipsum dolor sit amet, consectetuer adipiscing elit, sed diam nonummy nibh euismod tincidunt</p>
  </div>
  <div class="card" style="left:141px;top:1452px">
    <svg class="card-icon" viewBox="0 0 60 60" fill="var(--blue)"><rect x="6" y="34" width="8" height="18"/><rect x="18" y="26" width="8" height="26"/><rect x="30" y="30" width="8" height="22"/><circle cx="48" cy="12" r="6"/><rect x="42" y="20" width="12" height="32" rx="3"/></svg>
    <h3 style="top:86px">Business Analyst</h3>
    <p style="top:120px">Lorem ipsum dolor sit amet, consectetuer adipiscing elit, sed diam nonummy nibh euismod tincidunt</p>
  </div>
  <div class="card" style="left:469px;top:1452px">
    <div class="brand" style="position:absolute;left:0;width:100%;top:34px;flex-direction:column;gap:6px;font-size:30px;font-weight:600"><span class="brand-dot" style="width:40px;height:40px"></span>VelTarix</div>
    <svg class="abs" style="left:60px;top:134px" width="32" height="32" viewBox="0 0 24 24"><circle cx="12" cy="12" r="11" fill="none" stroke="var(--green)" stroke-width="1.6"/><path d="M8.5 10.5a8 8 0 0 0 5 5l1.4-1.4 2 1V17a1 1 0 0 1-1 1A10 10 0 0 1 6 8a1 1 0 0 1 1-1h1.9l1 2z" fill="var(--green)"/></svg>
    <div class="abs" style="left:102px;top:132px;text-align:left;color:var(--blue)"><div style="font-size:12.5px">Call Us Today</div><div style="font-size:16px">123.456.7890</div></div>
  </div>
  <div class="card" style="left:795px;top:1452px">
    <svg class="card-icon" viewBox="0 0 60 60" fill="none" stroke="var(--blue)" stroke-width="2.5"><rect x="24" y="8" width="30" height="24"/><path d="M30 26l6-8 5 5 7-9"/><circle cx="14" cy="14" r="5"/><path d="M8 52V24h12l8 8M12 52V38M16 52V38"/></svg>
    <h3 style="top:86px">Schulungen</h3>
    <p style="top:120px">Lorem ipsum dolor sit amet, consectetuer adipiscing elit, sed diam nonummy nibh euismod tincidunt</p>
  </div>

  <!-- BENEFITS -->
  <svg class="abs" style="left:640px;top:1730px" width="560" height="645" aria-hidden="true">
    <defs><linearGradient id="leaf" x1="0" y1="0" x2="1" y2="1"><stop offset="0" stop-color="#9ccf4f"/><stop offset="1" stop-color="#5e9a2c"/></linearGradient></defs>
    <path d="M560 0 V640 C510 560 470 520 400 490 C300 450 230 420 170 360 C120 300 160 220 180 150 C210 60 330 10 560 0 Z" fill="url(#leaf)"/>
  </svg>
  <h2 class="abs benefit-title">5 Vorteile von<br><span class="accent">Output Management Systems</span></h2>
  <ul class="abs benefit-list">
    <li style="height:33px"><svg width="14" height="14" viewBox="0 0 16 16"><circle cx="8" cy="8" r="7" fill="none" stroke="var(--blue)" stroke-width="1.5"/><path d="M4.5 8.2l2.3 2.3 4.7-4.7" fill="none" stroke="var(--blue)" stroke-width="1.6"/></svg>OMS vereinfacht und beschleunigt die Kommunikation mit Außen.</li>
    <li style="height:33px"><svg width="14" height="14" viewBox="0 0 16 16"><circle cx="8" cy="8" r="7" fill="none" stroke="var(--blue)" stroke-width="1.5"/><path d="M4.5 8.2l2.3 2.3 4.7-4.7" fill="none" stroke="var(--blue)" stroke-width="1.6"/></svg>Hilft dabei Fehler bei der Kommunikation zu reduzieren.</li>
    <li style="height:33px"><svg width="14" height="14" viewBox="0 0 16 16"><circle cx="8" cy="8" r="7" fill="none" stroke="var(--blue)" stroke-width="1.5"/><path d="M4.5 8.2l2.3 2.3 4.7-4.7" fill="none" stroke="var(--blue)" stroke-width="1.6"/></svg>Kunden erhalten schnell und sicher antworten auf Ihre Fragen.</li>
    <li style="height:55px"><svg width="14" height="14" viewBox="0 0 16 16"><circle cx="8" cy="8" r="7" fill="none" stroke="var(--blue)" stroke-width="1.5"/><path d="M4.5 8.2l2.3 2.3 4.7-4.7" fill="none" stroke="var(--blue)" stroke-width="1.6"/></svg>Mitarbeiter können sich auf das wesentliche konzentrieren, da sie auf vorbereitete Vorlagen zurückgreifen können.</li>
    <li><svg width="14" height="14" viewBox="0 0 16 16"><circle cx="8" cy="8" r="7" fill="none" stroke="var(--blue)" stroke-width="1.5"/><path d="M4.5 8.2l2.3 2.3 4.7-4.7" fill="none" stroke="var(--blue)" stroke-width="1.6"/></svg>Unternehmen erhalten vollständige Transparenz über Ihre Kommunikation</li>
  </ul>
  <div class="btn" style="left:141px;top:2114px;width:142px;height:39px;font-weight:400">Call Us Today</div>
  <div class="abs" role="img" aria-label="Photo of a smiling consultant working on a laptop in a bright office" style="left:675px;top:1847px;width:416px;height:304px;border-radius:8px;border:3px solid #fff;box-shadow:0 6px 20px rgba(0,0,0,.2);background:linear-gradient(110deg,#f2f3f5 0%,#dfe3e8 45%,#5b6f86 70%,#2c3d55 100%)"></div>

  <!-- TEAM -->
  <svg class="abs" style="left:0;top:2360px" width="1200" height="600" aria-hidden="true">
    <defs><linearGradient id="mist2" x1="0" y1="0" x2="0" y2="1"><stop offset="0" stop-color="#fff"/><stop offset="1" stop-color="#e3e9f3"/></linearGradient></defs>
    <path d="M0 0 H1200 V490 C1080 470 980 500 840 530 C680 565 560 560 400 548 C240 536 120 560 0 590 Z" fill="url(#mist2)"/>
  </svg>
  <h2 class="section-title" style="top:2380px;font-weight:600">Our <span class="accent">Team</span></h2>
  <div class="title-mark" style="top:2432px"></div>
  <div class="member" style="left:130px;top:2486px"><div class="member-photo"><div role="img" aria-label="Portrait of Lena Hovarth" style="background:linear-gradient(160deg,#d9d9d9,#5a5a5a)"></div></div><h4>Lena Hovarth</h4><div class="role">Head of Operations</div><p>Ut wisi enim ad minim veniam, quis nostruUt wisi enim a nostrud exd minim.</p></div>
  <div class="member" style="left:364px;top:2484px"><div class="member-photo"><div role="img" aria-label="Portrait of Mira Castell" style="background:linear-gradient(160deg,#e9d3bf,#6a4a3a)"></div></div><h4>Mira Castell</h4><div class="role">Product Lead</div><p>Ut wisi enim ad minim veniam, quis nostruUt wisi enim a nostrud exd minim.</p></div>
  <div class="member" style="left:599px;top:2484px"><div class="member-photo"><div role="img" aria-label="Portrait of Jonas Treval" style="background:linear-gradient(160deg,#4d6b3f,#8a4a55)"></div></div><h4>Jonas Treval</h4><div class="role">CEO</div><p>Ut wisi enim ad minim veniam, quis nostruUt wisi enim a nostrud exd minim.</p></div>
  <div class="member" style="left:835px;top:2486px"><div class="member-photo"><div role="img" aria-label="Portrait of Paul Dremont" style="background:linear-gradient(160deg,#cfc3b5,#6b5240)"></div></div><h4>Paul Dremont</h4><div class="role">Co-Founder, Advisor</div><p>Ut wisi enim ad minim veniam, quis nostruUt wisi enim a nostrud exd minim.</p></div>
  <div class="btn" style="left:505px;top:2785px;width:155px;height:40px">Meet Our Team</div>

  <!-- PARTNERS -->
  <h2 class="section-title" style="top:3000px;font-size:30px;font-weight:400">Our <span class="accent">Partners</span></h2>
  <div class="title-mark" style="top:3053px"></div>
  <div class="partner" style="left:161px"><div class="partner-badge"></div></div>
  <div class="partner" style="left:309px"><div class="partner-badge" style="background:#a9d477"></div></div>
  <div class="partner" style="left:457px"><div class="partner-badge" style="background:#9aa9b8"></div></div>
  <div class="partner" style="left:604px"><div class="partner-badge" style="background:#7d8794"></div></div>
  <div class="partner" style="left:752px"><div class="partner-badge" style="width:50px;height:50px;border-radius:50%;background:#2aa3a0"></div></div>
  <div class="partner" style="left:900px"><div class="partner-badge" style="background:#8fb3cf"></div></div>
  <div class="slider-dot" style="left:539px"></div>
  <div class="slider-dot" style="left:572px"></div>

  <!-- CONTACT -->
  <svg class="abs" style="left:0;top:3290px" width="620" height="650" role="img" aria-label="City skyline at dusk in deep blue tones">
    <defs><linearGradient id="city" x1="0" y1="0" x2="1" y2="1"><stop offset="0" stop-color="#2a4f7a"/><stop offset="1" stop-color="#142c4a"/></linearGradient></defs>
    <path d="M0 10 C120 -10 260 40 380 90 C520 150 600 200 560 300 C520 420 340 460 200 470 C100 480 30 560 0 640 Z" fill="url(#city)"/>
  </svg>
  <div class="abs" role="img" aria-label="Photo of hands typing on a laptop beside a coffee cup and a small plant" style="left:120px;top:3415px;width:431px;height:318px;border-radius:10px;background:linear-gradient(120deg,#ffffff 0%,#f1f2f4 50%,#c9ccd1 100%);box-shadow:0 8px 24px rgba(0,0,0,.25)"></div>
  <h2 class="abs contact-title">Quick <span class="accent">Contact</span></h2>
  <div class="field" style="left:568px;top:3493px;width:217px"><svg class="ico" viewBox="0 0 16 16"><circle cx="8" cy="5" r="3.2" fill="var(--blue)"/><path d="M2 15c0-3.5 2.7-5.5 6-5.5s6 2 6 5.5z" fill="var(--blue)"/></svg><span style="border-left:1px solid var(--line);padding-left:10px">First Name*</span></div>
  <div class="field" style="left:815px;top:3493px;width:225px"><svg class="ico" viewBox="0 0 16 16"><circle cx="8" cy="5" r="3.2" fill="var(--blue)"/><path d="M2 15c0-3.5 2.7-5.5 6-5.5s6 2 6 5.5z" fill="var(--blue)"/></svg><span style="border-left:1px solid var(--line);padding-left:10px">Last Name*</span></div>
  <div class="field" style="left:568px;top:3544px;width:217px"><svg class="ico" viewBox="0 0 24 24"><path d="M6.6 10.8a15 15 0 0 0 6.6 6.6l2.2-2.2c.3-.3.7-.4 1-.2 1.1.4 2.3.6 3.6.6.6 0 1 .4 1 1V20c0 .6-.4 1-1 1A17 17 0 0 1 3 4c0-.6.4-1 1-1h3.5c.6 0 1 .4 1 1 0 1.3.2 2.5.6 3.6.1.3 0 .7-.2 1z" fill="var(--blue)"/></svg><span style="border-left:1px solid var(--line);padding-left:10px">Your Phone*</span></div>
  <div class="field" style="left:815px;top:3544px;width:225px"><svg class="ico" viewBox="0 0 16 16"><rect x="1" y="3" width="14" height="10" rx="1" fill="var(--blue)"/><path d="M1.5 4l6.5 5 6.5-5" fill="none" stroke="#fff" stroke-width="1.2"/></svg><span style="border-left:1px solid var(--line);padding-left:10px">Your Email*</span></div>
  <div class="field" style="left:568px;top:3600px;width:472px;height:74px;align-items:flex-start;padding-top:10px"><svg class="ico" viewBox="0 0 16 16"><path d="M2 3h9a1 1 0 0 1 1 1v5a1 1 0 0 1-1 1H6l-3 3v-3H2a1 1 0 0 1-1-1V4a1 1 0 0 1 1-1z" fill="var(--blue)"/></svg><span style="border-left:1px solid var(--line);padding-left:10px">Your Message*</span></div>
  <div class="btn" style="left:568px;top:3697px;width:95px;height:36px;font-weight:600">Submit</div>

  <!-- FOOTER -->
  <div class="foot-col" style="left:143px"><h5>Quick Links</h5><ul><li>Home</li><li>About Us</li><li>Services</li><li>Careers</li><li>Contact Us</li></ul></div>
  <div class="foot-col" style="left:303px"><h5>Contact Details</h5>
    <div class="foot-row"><svg width="14" height="18" viewBox="0 0 14 18"><path d="M7 1a6 6 0 0 1 6 6c0 4.5-6 10-6 10S1 11.5 1 7a6 6 0 0 1 6-6z" fill="var(--green)"/><circle cx="7" cy="7" r="2.2" fill="#fff"/></svg><span>Street Name, City Name<br>State Zipcode</span></div>
    <div class="foot-row" style="margin-top:20px"><svg width="16" height="16" viewBox="0 0 24 24"><circle cx="12" cy="12" r="11" fill="none" stroke="var(--green)" stroke-width="1.8"/><path d="M8.5 10.5a8 8 0 0 0 5 5l1.4-1.4 2 1V17a1 1 0 0 1-1 1A10 10 0 0 1 6 8a1 1 0 0 1 1-1h1.9l1 2z" fill="var(--green)"/></svg><span>123.456.7890</span></div>
    <div class="foot-row" style="margin-top:18px"><svg width="16" height="16" viewBox="0 0 16 16"><rect x="1" y="3" width="14" height="10" rx="1" fill="none" stroke="var(--green)" stroke-width="1.5"/><path d="M1.5 4l6.5 5 6.5-5" fill="none" stroke="var(--green)" stroke-width="1.5"/></svg><span>inquiry@veltarix.com</span></div>
  </div>
  <div class="foot-col" style="left:579px;width:200px"><h5>Newsletter Signup</h5>
    <p style="margin-top:16px;font-size:12.5px;line-height:19px">Lorem Ispum is the dummy text of the industry</p>
    <div style="margin-top:12px;width:193px;height:30px;border:1px solid var(--line);border-radius:15px;font-size:11px;color:var(--muted);padding:6px 14px">enter email address</div>
    <div style="margin-top:8px;width:124px;height:30px;border-radius:15px;background:var(--green);color:#fff;font-size:14px;display:flex;align-items:center;justify-content:center">Subscribe</div>
  </div>
  <div class="foot-col" style="left:853px"><h5>Follow Us On</h5>
    <div style="display:flex;gap:9px;margin-top:18px">
      <span style="width:24px;height:24px;border:1.5px solid var(--blue);border-radius:50%"></span>
      <span style="width:24px;height:24px;border:1.5px solid var(--blue);border-radius:50%"></span>
      <span style="width:24px;height:24px;border:1.5px solid var(--blue);border-radius:50%"></span>
    </div>
  </div>
  <div class="abs brand" style="left:845px;top:4086px;font-size:28px"><span class="brand-dot" style="width:36px;height:36px"></span>VelTarix</div>
  <div class="abs copyright">Copyright © 2019 VelTarix. All Rights Reserved.</div>
</div>
</body>
</html>
```